Do i have coronavirus, flue or cold?

Using information from PFA and government agencies we want to make a easy to read infographic helping patients see if they have coronavirus, the flu or a cold. Using a flow diagram or whatever you think will make it easy to read and digest for the average lamen.

Information is in the word document and in the chart.

We are www.calvexa.co.uk attached is our brand guidelines, we will be putting this infographic on our website and email/sms it to all of our 300,000 patients.

```html
<!DOCTYPE html>
<html lang="en">
<head>
<meta charset="utf-8">
<title>Do I have Coronavirus, the Flu or a Cold?</title>
<link href="https://fonts.googleapis.com/css2?family=Oswald:wght@500;600&family=Alfa+Slab+One&family=Roboto:ital,wght@0,700;1,700&display=swap" rel="stylesheet">
<style>
:root{
  --navy:#2e3d8a;
  --ink:#141a44;
  --head-text:#3a4aa0;
  --head-tint:#d0d9ee;
  --blue-1:#5a6ab0;
  --blue-2:#6278b8;
  --blue-3:#7a93c8;
  --blue-side:#eef6f9;
  --orange-1:#ef663a;
  --orange-2:#f07a4a;
  --orange-3:#f39477;
  --orange-side:#f5a07e;
  --accent:#f05a23;
  --cream:#fdf0e6;
  --white:#ffffff;
}
*{box-sizing:border-box;margin:0;padding:0}
html,body{width:1200px;height:2429px;overflow:hidden;background:var(--white)}
.canvas{position:relative;width:1200px;height:2429px;background:var(--white)}
.title-bar{position:absolute;left:0;top:0;width:1170px;height:120px;background:var(--navy);
  display:flex;align-items:center;justify-content:center;
  font-family:'Oswald',sans-serif;font-weight:600;font-size:60px;color:var(--white);letter-spacing:1px}
.chart{position:absolute;left:14px;top:127px;width:1141px;display:grid;
  grid-template-columns:370px 253px 250px 251px;column-gap:2px;row-gap:2px}
.chart .col-symptom{margin-right:11px}
.col-head{height:97px;display:flex;align-items:center;justify-content:center;
  font-family:'Roboto',sans-serif;font-weight:700;font-size:32px;color:var(--head-text);
  box-shadow:0 2px 4px rgba(0,0,0,.12);margin-bottom:5px}
.col-head.tint{background:var(--head-tint)}
.col-head.plain{background:var(--white)}
.symptom{position:relative;height:194px;overflow:hidden}
.symptom.blue{background:var(--blue-side)}
.symptom.orange{background:var(--orange-side)}
.symptom .art{position:absolute;left:40px;top:14px;width:150px;height:166px;border-radius:12px;
  background:linear-gradient(160deg,#c9d6ec,#7d8fc6);z-index:0}
.symptom.orange .art{top:12px;width:170px;height:170px;border-radius:50%;
  background:radial-gradient(circle at 50% 45%,#ffffff 55%,#e9eefb 100%)}
.symptom .label{position:absolute;right:22px;top:50%;transform:translateY(-50%);z-index:1;
  font-family:'Oswald',sans-serif;font-weight:500;font-size:38px;line-height:1.15;text-align:right;text-transform:uppercase}
.symptom.blue .label{color:var(--accent)}
.symptom.orange .label{color:var(--cream)}
.symptom .label.top{top:22px;transform:none}
.cell{height:194px;display:flex;flex-direction:column;align-items:center;justify-content:center;
  color:var(--white);font-family:'Alfa Slab One',serif;text-align:center}
.cell.big{font-size:62px;line-height:1}
.cell.small{font-size:31px}
.cell .note{font-family:'Roboto',sans-serif;font-style:italic;font-size:28px;margin-top:8px}
.b1{background:var(--blue-1)}.b2{background:var(--blue-2)}.b3{background:var(--blue-3)}
.o1{background:var(--orange-1)}.o2{background:var(--orange-2)}.o3{background:var(--orange-3)}
.info-band{position:absolute;left:17px;top:2016px;width:1133px;height:71px;
  background:linear-gradient(90deg,var(--accent) 0%,var(--accent) 40%,#f7b08f 72%,var(--white) 85%);
  box-shadow:0 2px 5px rgba(0,0,0,.1);display:flex;align-items:center;padding-left:72px;
  font-family:'Oswald',sans-serif;font-weight:600;font-size:38px;color:var(--white);letter-spacing:1px}
.info-text{position:absolute;left:56px;top:2116px;width:745px;
  font-family:'Roboto',sans-serif;font-weight:700;font-size:23px;line-height:30.5px;color:var(--accent)}
.virus-art{position:absolute;left:810px;top:2040px;width:360px;height:240px;
  background:radial-gradient(ellipse at 50% 45%,rgba(232,150,70,.55),rgba(255,255,255,0) 70%)}
.footer{position:absolute;left:0;top:2308px;width:1170px;height:121px;background:var(--ink);color:var(--white);
  font-family:'Roboto',sans-serif;font-weight:700;font-style:italic}
.footer .credit{position:absolute;top:30px;left:0;width:100%;display:flex;justify-content:center;align-items:center;gap:18px;font-size:24px}
.brand{display:flex;align-items:center;gap:8px;font-style:normal;font-size:28px}
.brand .mark{width:24px;height:24px;border-radius:50%;background:var(--white)}
.footer .source{position:absolute;top:86px;left:0;width:100%;text-align:center;font-size:22px}
</style>
</head>
<body>
<div class="canvas">
  <header class="title-bar">Do I have Coronavirus, the Flu or a Cold ?</header>

  <section class="chart">
    <div class="col-head plain col-symptom">Symptom</div>
    <div class="col-head tint">CORONAVIRUS</div>
    <div class="col-head plain">FLU</div>
    <div class="col-head tint">COLD</div>

    <div class="symptom blue col-symptom"><div class="art" role="img" aria-label="Illustration of a boy with a thermometer and fever"></div><div class="label top" style="top:52px">Fever</div></div>
    <div class="cell big b1">Yes</div>
    <div class="cell big b2">Yes<span class="note">High</span></div>
    <div class="cell small b3">Rare</div>

    <div class="symptom orange col-symptom"><div class="art" style="left:78px;width:166px;height:166px" role="img" aria-label="Illustration of a boy coughing"></div><div class="label top">Cough</div></div>
    <div class="cell big o1">Yes</div>
    <div class="cell big o2">Yes</div>
    <div class="cell small o3">Moderate</div>

    <div class="symptom blue col-symptom"><div class="art" style="left:28px;width:150px" role="img" aria-label="Illustration of a tired boy sleeping in bed"></div><div class="label top" style="top:44px">Tiredness</div></div>
    <div class="cell big b1">Yes</div>
    <div class="cell big b2">Yes</div>
    <div class="cell small b3">Mild</div>

    <div class="symptom orange col-symptom"><div class="art" style="left:6px;width:168px;height:168px" role="img" aria-label="Illustration of a boy short of breath"></div><div class="label" style="right:8px;font-size:36px">Shortness<br>of breath</div></div>
    <div class="cell big o1">Yes</div>
    <div class="cell big o2">Yes</div>
    <div class="cell small o3">Rare</div>

    <div class="symptom blue col-symptom"><div class="art" style="left:80px;width:130px" role="img" aria-label="Illustration of a boy with aching muscles"></div><div class="label" style="right:40px;text-align:center">Muscle<br>ache</div></div>
    <div class="cell big b1">Yes</div>
    <div class="cell big b2">Yes<span class="note">Often</span></div>
    <div class="cell small b3">Moderate</div>

    <div class="symptom orange col-symptom"><div class="art" style="left:12px;width:172px;height:172px" role="img" aria-label="Illustration of a boy holding his head with a headache"></div><div class="label top" style="top:34px;right:22px">Headache</div></div>
    <div class="cell small o1">Sometimes</div>
    <div class="cell big o2">Yes</div>
    <div class="cell small o3">Rare</div>

    <div class="symptom blue col-symptom"><div class="art" style="left:100px;width:120px" role="img" aria-label="Illustration of a boy with a scarf and sore throat"></div><div class="label" style="right:32px;text-align:center">Sore<br>throat</div></div>
    <div class="cell small b1">Sometimes</div>
    <div class="cell small b2">Sometimes</div>
    <div class="cell big b3">Yes</div>

    <div class="symptom orange col-symptom"><div class="art" style="left:18px;width:176px;height:176px" role="img" aria-label="Illustration of a boy blowing a runny nose"></div><div class="label" style="right:34px">Stuffy/<br>runny<br>nose</div></div>
    <div class="cell small o1">Rare</div>
    <div class="cell small o2">Sometimes</div>
    <div class="cell big o3">Yes</div>

    <div class="symptom blue col-symptom"><div class="art" style="left:70px;width:140px" role="img" aria-label="Illustration of a boy sneezing into a tissue"></div><div class="label top" style="top:40px">Sneezing</div></div>
    <div class="cell small b1">No</div>
    <div class="cell small b2">Sometimes</div>
    <div class="cell big b3">Yes</div>
  </section>

  <div class="info-band">CORONAVIRUS &nbsp;SYMPTOMS</div>
  <p class="info-text">The most common symptoms of COVID-19 are fever, tiredness, and dry cough. Some patients may have aches and pains, nasal congestion, runny nose, sore throat or diarrhoea. These symptoms are usually mild and begin gradually. Some people become infected but don’t develop any symptoms and don't feel unwell.</p>
  <div class="virus-art" role="img" aria-label="Decorative orange virus particles"></div>

  <footer class="footer">
    <div class="credit">Brought to you by: <span class="brand"><span class="mark"></span>Calvexa</span></div>
    <div class="source">Source: PFA, Public Health Standards Board</div>
  </footer>
</div>
</body>
</html>
```